Kestrel Gardenworks Business Card

An eye catching, yet simple business card that includes;

1. our logo
2. office phone - 5083172946
3. email - kestrelgardenworks@mailbrook.com
4. website - www.kestrelgardenworks.com
5. instagram - @kestrelgardenworksnv

```html
<!DOCTYPE html>
<html lang="en">
<head>
<meta charset="utf-8">
<title>Kestrel Gardenworks Business Card</title>
<link rel="stylesheet" href="https://fonts.googleapis.com/css2?family=Crimson+Text:wght@400;700&display=swap">
<style>
  :root {
    --page: #2b2b2b;
    --brown-light: #8c5224;
    --brown-mid: #5e3210;
    --brown-dark: #341903;
    --accent: #a0672f;
    --ink: #1c1c1c;
    --paper: #ffffff;
    --paper-shade: #eeeeee;
    --mark-light: rgba(255, 255, 255, 0.12);
    --mark-grey: rgba(0, 0, 0, 0.1);
    --rule: #c49a6c;
  }
  * { margin: 0; padding: 0; box-sizing: border-box; }
  html, body { width: 1200px; height: 900px; overflow: hidden; }
  body {
    background: var(--page);
    font-family: "Crimson Text", Georgia, serif;
    position: relative;
  }
  .card {
    position: absolute;
    left: 240px;
    width: 720px;
    height: 411px;
    overflow: hidden;
    box-shadow: 0 10px 30px rgba(0, 0, 0, 0.45);
  }
  .card--back {
    top: 30px;
    background: radial-gradient(ellipse at 30% 85%, var(--brown-light) 0%, var(--brown-mid) 45%, var(--brown-dark) 100%);
  }
  .card--front {
    top: 469px;
    background: linear-gradient(160deg, var(--paper) 55%, var(--paper-shade) 100%);
  }
  .motif {
    position: absolute;
    left: 40px;
    top: 40px;
    width: 330px;
    height: 400px;
    border-radius: 45% 55% 30% 40%;
  }
  .card--back .motif { background: radial-gradient(ellipse, var(--mark-light) 0%, rgba(255,255,255,0.04) 70%, transparent 100%); }
  .card--front .motif { background: radial-gradient(ellipse, var(--mark-grey) 0%, rgba(0,0,0,0.03) 70%, transparent 100%); }
  .site-line {
    position: absolute;
    left: 40px;
    top: 38px;
    color: var(--paper);
    font-size: 15px;
    letter-spacing: 6px;
  }
  .brand {
    position: absolute;
    right: 40px;
    display: flex;
    align-items: center;
    gap: 14px;
  }
  .card--back .brand { top: 165px; }
  .card--front .brand { top: 60px; }
  .brand-dot {
    width: 26px; height: 26px; border-radius: 50%;
    background: var(--accent);
    flex: none;
  }
  .brand-name {
    font-size: 44px;
    font-weight: 700;
    line-height: 1;
    letter-spacing: 1px;
  }
  .card--back .brand-name { color: var(--paper); }
  .card--front .brand-name { color: var(--ink); }
  .contacts {
    position: absolute;
    left: 32px;
    right: 32px;
    bottom: 30px;
    color: var(--ink);
    font-size: 14px;
    white-space: nowrap;
  }
  .contact-row { display: flex; align-items: center; gap: 6px; }
  .contact-row + .contact-row { margin-top: 6px; }
  .rule { flex: 1; height: 1px; background: var(--rule); margin-left: 12px; }
  .sep { color: #777; margin: 0 3px; }
  .icon { width: 14px; height: 14px; flex: none; }
  .social-dot {
    width: 12px; height: 12px; border-radius: 50%;
    background: var(--accent); flex: none;
  }
</style>
</head>
<body>
  <section class="card card--back">
    <div class="motif" role="img" aria-label="Faint large leaping animal silhouette decoration"></div>
    <p class="site-line">www.kestrelgardenworks.com</p>
    <div class="brand">
      <span class="brand-dot"></span>
      <span class="brand-name">Kestrel Gardenworks</span>
    </div>
  </section>

  <section class="card card--front">
    <div class="motif" role="img" aria-label="Faint grey leaping animal silhouette decoration"></div>
    <div class="brand">
      <span class="brand-dot"></span>
      <span class="brand-name">Kestrel Gardenworks</span>
    </div>
    <div class="contacts">
      <div class="contact-row">
        <svg class="icon" viewBox="0 0 24 24" aria-hidden="true"><path fill="#a0672f" d="M6.6 10.8a15 15 0 0 0 6.6 6.6l2.2-2.2a1 1 0 0 1 1-.25 11.4 11.4 0 0 0 3.6.57 1 1 0 0 1 1 1V20a1 1 0 0 1-1 1A17 17 0 0 1 3 4a1 1 0 0 1 1-1h3.5a1 1 0 0 1 1 1c0 1.25.2 2.45.57 3.57a1 1 0 0 1-.25 1z"/></svg>
        <span>5083172946</span>
        <span class="rule"></span>
      </div>
      <div class="contact-row">
        <svg class="icon" viewBox="0 0 24 24" aria-hidden="true"><rect x="2" y="5" width="20" height="14" rx="1" fill="#a0672f"/><path d="M3 6l9 7 9-7" fill="none" stroke="#fff" stroke-width="1.6"/></svg>
        <span>kestrelgardenworks@mailbrook.com</span>
        <span class="sep">|</span>
        <svg class="icon" viewBox="0 0 24 24" aria-hidden="true"><g fill="none" stroke="#a0672f" stroke-width="1.8"><circle cx="12" cy="12" r="9"/><ellipse cx="12" cy="12" rx="4" ry="9"/><path d="M3 12h18M5 7h14M5 17h14"/></g></svg>
        <span>www.kestrelgardenworks.com</span>
        <span class="sep">|</span>
        <span class="social-dot"></span>
        <span>@kestrelgardenworksnv</span>
      </div>
    </div>
  </section>
</body>
</html>
```